Quorvel Lab - Business Cards & Stationary
Layouts for B-cards, Letterhead, Powerpoint Templates
Quorvel Lab - Business Cards & Stationary -
Creative Brief
Professional
Desmond Pelly
Director of Product Development
4852 Amberfield Lane Dallas, Texas 75391-4418
des.pelly@quorvellabs.example

```html
<!DOCTYPE html>
<html lang="en">
<head>
<meta charset="utf-8">
<title>Quorvel Lab – Business Cards</title>
<link href="https://fonts.googleapis.com/css2?family=Arimo:wght@400;700&display=swap" rel="stylesheet">
<style>
  :root {
    --stage: #8f8f8f;
    --card-light: #ffffff;
    --card-dark-top: #2b2b2b;
    --card-dark-bottom: #0d0d0d;
    --brand-brown: #6b4520;
    --brand-gold: #b8893d;
    --name-brown: #8a5a2b;
    --label-accent: #d2622a;
    --ink-dark: #2a2a2a;
    --ink-light: #e6e6e6;
    --rule-light: #9a9a9a;
    --rule-dark: #6a6a6a;
  }
  * { box-sizing: border-box; margin: 0; padding: 0; }
  html, body { width: 1200px; height: 792px; overflow: hidden; }
  body {
    background: var(--stage);
    font-family: "Arimo", Arial, sans-serif;
    position: relative;
  }
  .card {
    position: absolute;
    width: 464px;
    height: 272px;
    border-radius: 18px;
    overflow: hidden;
  }
  .card--light { background: var(--card-light); color: var(--ink-dark); }
  .card--dark {
    background: linear-gradient(180deg, var(--card-dark-top), var(--card-dark-bottom));
    color: var(--ink-light);
  }
  .front-light { left: 132px; top: 100px; }
  .front-dark  { left: 628px; top: 100px; }
  .back-light  { left: 132px; top: 420px; }
  .back-dark   { left: 628px; top: 420px; }

  .brand {
    position: absolute;
    left: 50px;
    top: 44px;
    display: flex;
    align-items: center;
    gap: 14px;
  }
  .brand__mark { width: 40px; height: 40px; border-radius: 6px; }
  .brand__name { font-size: 46px; font-weight: 700; letter-spacing: -0.5px; }
  .card--light .brand__mark { background: var(--brand-brown); }
  .card--light .brand__name { color: var(--brand-brown); }
  .card--dark .brand__mark { background: var(--brand-gold); }
  .card--dark .brand__name { color: var(--brand-gold); }

  .holder {
    position: absolute;
    left: 30px;
    top: 136px;
    width: 160px;
  }
  .holder__name { font-size: 17px; font-weight: 700; color: var(--name-brown); }
  .holder__title { font-size: 10.5px; margin-top: 3px; }

  .contact {
    position: absolute;
    left: 198px;
    top: 134px;
    padding-left: 12px;
    font-size: 11.5px;
    line-height: 1.45;
  }
  .card--light .contact { border-left: 1px solid var(--rule-light); }
  .card--dark .contact { border-left: 1px solid var(--rule-dark); }
  .contact__label { color: var(--label-accent); }

  .back-brand {
    position: absolute;
    inset: 0;
    display: flex;
    align-items: center;
    justify-content: center;
    gap: 10px;
  }
  .back-brand .brand__mark { width: 28px; height: 28px; border-radius: 5px; }
  .back-brand .brand__name { font-size: 26px; }
</style>
</head>
<body>

  <section class="card card--light front-light">
    <div class="brand">
      <span class="brand__mark"></span>
      <span class="brand__name">Quorvel Lab</span>
    </div>
    <div class="holder">
      <p class="holder__name">Desmond Pelly</p>
      <p class="holder__title">Director of Product Development</p>
    </div>
    <div class="contact">
      <p>4852 Amberfield Lane</p>
      <p>Dallas, Texas 75391-4418</p>
      <p><span class="contact__label">Cell :</span> 555.014.2290</p>
      <p><span class="contact__label">Email :</span> des.pelly@quorvellabs.example</p>
    </div>
  </section>

  <section class="card card--dark front-dark">
    <div class="brand">
      <span class="brand__mark"></span>
      <span class="brand__name">Quorvel Lab</span>
    </div>
    <div class="holder">
      <p class="holder__name">Desmond Pelly</p>
      <p class="holder__title">Director of Product Development</p>
    </div>
    <div class="contact">
      <p>4852 Amberfield Lane</p>
      <p>Dallas, Texas 75391-4418</p>
      <p><span class="contact__label">Cell :</span> 555.014.2290</p>
      <p><span class="contact__label">Email :</span> des.pelly@quorvellabs.example</p>
    </div>
  </section>

  <section class="card card--light back-light">
    <div class="back-brand">
      <span class="brand__mark"></span>
      <span class="brand__name">Quorvel Lab</span>
    </div>
  </section>

  <section class="card card--dark back-dark">
    <div class="back-brand">
      <span class="brand__mark"></span>
      <span class="brand__name">Quorvel Lab</span>
    </div>
  </section>

</body>
</html>
```